Coffee Bag Label

I need a coffee bag label designed (front label and back label):
Our company "Tidy-Pod" imports organic coffee beans direct from a farm on Vorsela Mountain on a private reserve (rainforest) from Jinotega, Nicaragua.
Labels should each be 3 inches x 3 inches (with room on edges for bleed). I want the front label to catch the eye and coordinate well with the coffee bag. The bags sizes are below and pictures are attached.
Bag sizes: Lime green 12 oz bag: 3-3/8" x 2-9/16" x 10-1/4"
Black 2 oz sample stand up pouch: 4" x 6-1/2" + 2-3/8", 2oz (60g)
Black 2lb bag: 5" x 3-3/8" x 15", 2lb (1kg)
Please include as much as possible below on the front label without it looking too wordy:
1) Our logo (it's attached). Feel free to do something creative with just the bean and place "Tidy-Pod" or "Tidy-Pod Coffees" somewhere else. They don't have to be together like in the attached file. The bean can be in the background of the label as well or something else cool like in the form of a cloud over the volcano or as the sun in the sky over the volcano.
2) lime green, burnt orange, dark brown & black
3) Front label should say:
"100% Premium Arabica Nicaraguan Coffee"
"Organic, Rain Forest & Mountain Shade Grown"
Bottom of label:
"Medium Roast"
"Full body, bold flavor, nutty, hints of chocolate, with a distinct & flavorful aroma."
I want one front label file for each size bag: "2 oz" "12 oz" & "32 oz"
Back of the label:
I have uploaded a hand drawn pic of what I am thinking but if you have a better idea please submit it.
Please include as much as possible below without it looking wordy:
Directions on the perfect cup:
***2 Tbsp high quality coffee 6 Oz. cup of pure filtered water
(these can be tied into the hand-drawn picture. I will label the section each one corresponds to)
Organically Grown (sustainable)
Rainforest Grown (sustainable)
Mountain Shade Grown (sustainable)
Hand Picked (select)
Spring Water Washed (select)
Sun Dried (select)
Social Responsibility (profits help fund Bright Path Outreach Nicaragua www.brightpathoutreach.example.org)
Single Source Coffee (Single source)
Traceable Source (single source)
Website: www.Tidy-Pod.example.com
Reason: I have been asked to extend deadline by a few designers.
Thanks,
Joanne Pelter
ages 18-54
- Should have a cool border. Maybe fade from one color to another or have something more original than just a 3x3 square border.

```html
<!DOCTYPE html>
<html lang="en">
<head>
<meta charset="utf-8">
<title>Tidy-Pod Coffee Labels</title>
<link rel="stylesheet" href="https://fonts.googleapis.com/css2?family=PT+Sans+Narrow:wght@400;700&display=swap">
<style>
  :root {
    --cream: #fdf9f1;
    --burnt-orange: #f48a4f;
    --orange-light: #f7a06d;
    --lime-light: #c9df87;
    --lime: #8fc640;
    --brown: #5a2a17;
    --arrow-green: #dcebb0;
    --white: #ffffff;
  }
  html, body {
    margin: 0;
    width: 1200px;
    height: 1000px;
    overflow: hidden;
    background: var(--cream);
    font-family: "PT Sans Narrow", "Arial Narrow", sans-serif;
  }
  .canvas { position: relative; width: 1200px; height: 1000px; }
  .label { position: absolute; top: 185px; width: 480px; height: 629px; }
  .label--front { left: 90px; }
  .label--back { left: 630px; }
  .band-orange { fill: var(--burnt-orange); }
  .band-lime-light { fill: var(--lime-light); }
  .band-lime { fill: var(--lime); }
  .edge { fill: none; stroke: var(--lime); stroke-width: 4; }
  .inner-frame { fill: none; stroke: var(--white); stroke-width: 2.5; stroke-linejoin: round; }
  .txt { font-family: "PT Sans Narrow", "Arial Narrow", sans-serif; fill: var(--brown); text-anchor: middle; }
  .txt--bold { font-weight: 700; }
  .txt--white { fill: var(--white); }
  .brand-name { font-size: 34px; font-weight: 700; fill: var(--brown); letter-spacing: 0.5px; }
  .cycle-arrow { fill: none; stroke: var(--arrow-green); stroke-width: 4; }
</style>
</head>
<body>
<main class="canvas">

  <!-- Front label -->
  <svg class="label label--front" viewBox="0 0 360 472" aria-label="Tidy-Pod front label">
    <defs>
      <clipPath id="front-shape"><path d="M180 0 L360 472 L0 472 Z"/></clipPath>
    </defs>
    <g clip-path="url(#front-shape)">
      <rect class="band-lime" x="0" y="0" width="360" height="472"/>
      <path class="band-lime-light" d="M0 0 H360 V358 Q270 350 180 356 T0 352 Z"/>
      <path class="band-orange" d="M0 0 H360 V276 Q270 284 180 278 T0 280 Z"/>
    </g>
    <path class="edge" d="M180 2 L358 470 L2 470 Z"/>
    <path class="inner-frame" d="M180 24 L340 461 L20 461 Z"/>

    <circle cx="180" cy="168" r="34" fill="var(--brown)"/>
    <text class="txt brand-name" x="180" y="246">Tidy-Pod</text>

    <text class="txt txt--bold" x="180" y="295" font-size="17">100% Premium</text>
    <text class="txt txt--bold" x="180" y="320" font-size="17">Arabica Nicaraguan Coffee</text>
    <text class="txt" x="180" y="343" font-size="12.5">Organic, Rain Forest &amp; Mountain Shade Grown</text>

    <text class="txt txt--bold txt--white" x="180" y="381" font-size="25">Medium Roast</text>
    <text class="txt" x="180" y="404" font-size="13.5">Full body, bold flavor, nutty, hints of chocolate,</text>
    <text class="txt" x="180" y="426" font-size="13.5">with a distinct &amp; flavorful aroma.</text>
    <text class="txt txt--bold" x="180" y="454" font-size="18">12 oz</text>
  </svg>

  <!-- Back label -->
  <svg class="label label--back" viewBox="0 0 360 472" aria-label="Tidy-Pod back label">
    <defs>
      <clipPath id="back-shape"><path d="M180 0 L360 472 L0 472 Z"/></clipPath>
      <marker id="arrow-head" viewBox="0 0 10 10" refX="5" refY="5" markerWidth="4" markerHeight="4" orient="auto">
        <path d="M0 0 L10 5 L0 10 Z" fill="var(--arrow-green)"/>
      </marker>
    </defs>
    <g clip-path="url(#back-shape)">
      <rect class="band-lime" x="0" y="0" width="360" height="472"/>
      <path class="band-lime-light" d="M0 0 H360 V282 Q270 276 180 282 T0 280 Z"/>
      <path class="band-orange" d="M0 0 H360 V180 Q270 188 180 182 T0 186 Z"/>
      <path role="img" aria-label="Scattered coffee bean pattern" fill="var(--orange-light)" opacity="0.55"
            d="M180 30 L228 160 Q180 168 132 160 Z"/>
    </g>
    <path class="edge" d="M180 2 L358 470 L2 470 Z"/>
    <path class="inner-frame" d="M180 24 L340 461 L20 461 Z"/>

    <text class="txt txt--bold" x="180" y="210" font-size="19">Directions on</text>
    <text class="txt txt--bold" x="180" y="233" font-size="19">the perfect cup:</text>
    <text class="txt" x="180" y="254" font-size="13.5">2 Tbsp high quality coffee</text>
    <text class="txt" x="180" y="273" font-size="13.5">6 Oz. cup of pure filtered water</text>

    <path class="cycle-arrow" d="M152 330 A38 38 0 0 1 214 368" marker-end="url(#arrow-head)"/>
    <path class="cycle-arrow" d="M206 384 A38 38 0 0 1 142 346" marker-end="url(#arrow-head)"/>

    <text class="txt txt--white" x="114" y="308" font-size="12">Single Source</text>
    <text class="txt txt--white" x="122" y="325" font-size="10.5">Coffee</text>
    <text class="txt txt--white" x="122" y="338" font-size="10.5">Traceable</text>
    <text class="txt txt--white" x="122" y="351" font-size="10.5">Source</text>

    <text class="txt txt--white" x="232" y="308" font-size="12">Sustainable</text>
    <text class="txt txt--white" x="230" y="325" font-size="10.5" text-anchor="start">Organically,</text>
    <text class="txt txt--white" x="230" y="338" font-size="10.5" text-anchor="start">Rainforest ,</text>
    <text class="txt txt--white" x="230" y="351" font-size="10.5" text-anchor="start">Mountain Shade</text>
    <text class="txt txt--white" x="230" y="364" font-size="10.5" text-anchor="start">Grown</text>

    <text class="txt" x="110" y="374" font-size="12">“Select”</text>
    <text class="txt" x="110" y="387" font-size="12">Nicaraguan</text>
    <text class="txt" x="110" y="400" font-size="12">Beans</text>
    <text class="txt txt--white" x="96" y="423" font-size="10.5">Hand Picked</text>
    <text class="txt txt--white" x="96" y="436" font-size="10.5">Spring Water Washed</text>
    <text class="txt txt--white" x="96" y="449" font-size="10.5">Sun Dried</text>

    <text class="txt" x="246" y="383" font-size="12">Social</text>
    <text class="txt" x="246" y="396" font-size="12">Responsibility</text>
    <text class="txt txt--white" x="242" y="418" font-size="10">profits help fund</text>
    <text class="txt txt--white" x="242" y="431" font-size="10">Bright Path Outreach Nicaragua</text>
    <text class="txt txt--white" x="242" y="444" font-size="9.5">www.brightpathoutreach.example.org</text>
  </svg>

</main>
</body>
</html>
```